Travel Group 'Lydgate Group' needs a new business card design

Lydgate Group is a diverse business specialising in bespoke, tailor made holidays to suit all budgets and we are specialists in planning exciting day/short trips to suit all markets. Our target market is very varied going from the corporate client and as well as people in the community who simply want to experience something special.
We are looking for a card design that will encourage people to look at our websites and social media platforms and to see for themselves the different facets to our business. It is essential that the card has social media icons for Facebook, Twitter and Instagram. We are looking for a card with a blank background with no pictures and for the front side to have the attached Lydgate logo. The card should have similar colour scheme to the attached Lydgate logo.
The card must have the following information on one side:
Maud Penrose
Business Development Manager
maudpenrose@lydgatevoyages.example
Lydgate Group, 87 Quarry Lane
Dunmarrow, Carrickvale, Scotland KA19 4TN
+44 (0)1632 730182
And then the card must have the following on the second side:
(Lydgate logo)
(social media icons)
www.lydgatevoyages.example
www.lydgateoutings.example
Target Market(s)
Our target market is very varied going from the corporate client and as well as people in the community who simply want to experience something special.
Industry/Entity Type
Business
Contact Information for Business Card
Maud Penrose
+44 (0)1632 730182
(Lydgate logo)
(social media icons)
www.lydgatevoyages.example
www.lydgateoutings.example
Requirements
Must have
- It is essential that the card has social media icons for Facebook, Twitter & Instagram.
Should not have
- Should not have any images other than Lydgate logo.

```html
<!DOCTYPE html>
<html lang="en">
<head>
<meta charset="utf-8">
<title>Lydgate Group – Business Card</title>
<link rel="stylesheet" href="https://fonts.googleapis.com/css2?family=Open+Sans:wght@400;600&family=Tinos:wght@700&display=swap">
<style>
  :root {
    --navy: #27215f;
    --magenta: #b5177f;
    --white: #ffffff;
    --backdrop: #ece9ee;
    --serif: "Tinos", "Times New Roman", serif;
    --sans: "Open Sans", Arial, sans-serif;
  }
  * { margin: 0; padding: 0; box-sizing: border-box; }
  html, body { width: 1200px; height: 900px; overflow: hidden; }
  body { background: var(--backdrop); position: relative; font-family: var(--sans); }

  .card { position: absolute; box-shadow: 0 6px 18px rgba(0,0,0,.18); }

  .card--contact {
    left: 78px; top: 34px; width: 588px; height: 363px;
    background: var(--navy); color: var(--white);
  }
  .holder-name {
    position: absolute; left: 31px; top: 48px;
    font-family: var(--serif); font-weight: 700; font-size: 21px;
    letter-spacing: .5px; text-transform: uppercase;
  }
  .holder-role { position: absolute; left: 30px; top: 73px; font-size: 15.5px; }

  .social-row { position: absolute; left: 30px; top: 129px; display: flex; gap: 8px; }
  .social-slot { width: 22px; height: 22px; background: var(--white); }

  .contact-list { position: absolute; left: 31px; top: 160px; list-style: none; }
  .contact-list li { display: flex; align-items: center; height: 21.3px; font-size: 15px; }
  .contact-list svg { width: 12px; height: 12px; margin-right: 9px; fill: var(--white); flex: none; }

  .address { position: absolute; left: 31px; top: 252px; font-size: 15px; line-height: 22px; font-style: normal; }

  .card--brand {
    left: 388px; top: 505px; width: 566px; height: 352px;
    background: var(--white);
    display: flex; align-items: center; justify-content: center; gap: 14px;
  }
  .brand-dot { width: 22px; height: 22px; border-radius: 50%; background: var(--magenta); }
  .brand-name {
    font-family: var(--serif); font-weight: 700; font-size: 34px;
    letter-spacing: 2px; color: var(--navy); text-transform: uppercase;
  }
</style>
</head>
<body>
  <section class="card card--contact" aria-label="Contact side">
    <h1 class="holder-name">Maud Penrose</h1>
    <p class="holder-role">Business Development Manager</p>

    <div class="social-row" aria-label="Social media">
      <span class="social-slot"></span>
      <span class="social-slot"></span>
      <span class="social-slot"></span>
    </div>

    <ul class="contact-list">
      <li><svg viewBox="0 0 12 12" aria-hidden="true"><path d="M1 3c0-1 1-2 2-2h6c1 0 2 1 2 2v1H8V3H4v1H1z M2 5h8l1 6H1z"/></svg>+44 (0)1632 730182</li>
      <li><svg viewBox="0 0 12 12" aria-hidden="true"><path d="M0 2h12v1L6 7 0 3z M0 4.5l6 4 6-4V10H0z"/></svg>maudpenrose@lydgatevoyages.example</li>
      <li><svg viewBox="0 0 12 12" aria-hidden="true"><circle cx="6" cy="6" r="5.5"/><path d="M3 4h3v2H4z M7 7h2v2H7z" fill="#27215f"/></svg>www.lydgatevoyages.example</li>
      <li><svg viewBox="0 0 12 12" aria-hidden="true"><circle cx="6" cy="6" r="5.5"/><path d="M3 4h3v2H4z M7 7h2v2H7z" fill="#27215f"/></svg>www.lydgateoutings.example</li>
    </ul>

    <address class="address">
      Lydgate Group, 87 Quarry Lane<br>
      Dunmarrow, Carrickvale,<br>
      Scotland KA19 4TN
    </address>
  </section>

  <section class="card card--brand" aria-label="Brand side">
    <span class="brand-dot" aria-hidden="true"></span>
    <span class="brand-name">Lydgate</span>
  </section>
</body>
</html>
```